4 Poster Designs required for Nail Salon

We require 4 poster designs that will be displayed inside a shopping centre. Each design should contain our logo and the words "Located next to TallMart" (or similar). Design 1 (MOTHERS DAY) should contain the words "Mothers Day Special" and "$10 gift voucher when you spend over $50". Design 2 (CHRISTMAS) should contain the words "Christmas in July" and "Purchase a set of nails and get a $10 gift voucher". Design 3 (ALL YEAR) should contain the words "New Deluxe Spa Pedicure Service" and the words "Try our new Deluxe Spa Pedicure and get a free nail buff, shape and polish for your fingernails". Design 4 (ALL YEAR 2)should contain high quality nail salon image(s) and the words "Now Open". We like designs that support our image of high quality/fun/clean and safe.
Updates
I will close this early. In 24 hours.
Target Market(s)
Rich mums
Industry/Entity Type
Shopping
Look and feel
Each slider illustrates characteristics of the customer's brand and the style your logo design should communicate.

```html
<!DOCTYPE html>
<html lang="en">
<head>
<meta charset="utf-8">
<title>Lacquer Nail Salon – Poster Set</title>
<link rel="stylesheet" href="https://fonts.googleapis.com/css2?family=Arimo:wght@400;700&family=Nunito:wght@900&family=Parisienne&family=Quicksand:wght@400&display=swap">
<style>
  :root {
    --pink: #e2509c;
    --pink-deep: #d93d8e;
    --pink-light: #f3a8cf;
    --pink-soft: #e97ab5;
    --pink-text: #ee3f97;
    --blue: #3d7cc4;
    --blue-light: #4a8fd6;
    --white: #ffffff;
    --ink: #444444;
    --green: #3fae49;
    --mauve: #c7a3b2;
  }
  * { box-sizing: border-box; margin: 0; padding: 0; }
  html, body { width: 1200px; height: 848px; overflow: hidden; background: var(--white); }
  .stage { position: relative; width: 1200px; height: 848px; }

  .poster {
    position: absolute;
    background: var(--white);
    box-shadow: 0 6px 18px rgba(0,0,0,.22);
    overflow: hidden;
  }
  .poster > * { position: absolute; }

  /* header */
  .brand {
    left: 0; top: 0;
    background: linear-gradient(90deg, var(--pink-deep), var(--pink-light));
    display: flex; flex-direction: column; justify-content: center;
    padding-left: 26px;
    font-family: "Quicksand", sans-serif; font-weight: 400; color: var(--white);
  }
  .brand-name { font-size: 44px; letter-spacing: 3px; line-height: 1; }
  .brand-sub { font-size: 13px; letter-spacing: 1px; margin-top: 4px; margin-left: 70px; }
  .locator {
    top: 0; right: 0; background: var(--white);
    display: flex; flex-direction: column; justify-content: center; align-items: center;
    font-family: "Arimo", sans-serif; color: var(--blue); text-align: center;
  }
  .locator-lead { font-weight: 700; font-size: 21px; line-height: 1.12; }
  .locator-store { font-weight: 400; font-size: 29px; color: var(--blue-light); line-height: 1.1; }

  .script { font-family: "Parisienne", cursive; white-space: nowrap; font-weight: 400; }
  .punch {
    font-family: "Nunito", sans-serif; font-weight: 900; color: var(--pink-text);
    -webkit-text-stroke: 6px var(--white); paint-order: stroke fill;
    text-shadow: 0 0 7px rgba(226,80,156,.7);
    white-space: nowrap; text-align: center; left: 0; right: 0; line-height: 1;
  }
  .footer {
    left: 0; right: 0; bottom: 0;
    display: flex; align-items: center; padding: 0 18px;
    font-family: "Arimo", sans-serif; font-size: 19px;
  }
  .social-box {
    margin-left: auto; width: 24px; height: 24px;
    border: 2px solid var(--white); border-radius: 3px;
  }

  /* Christmas */
  .poster-christmas { left: 31px; top: 40px; width: 418px; height: 588px; }
  .poster-christmas .brand { width: 268px; height: 127px; }
  .poster-christmas .locator { width: 150px; height: 127px; }
  .poster-christmas .title { top: 140px; left: 18px; font-size: 52px; color: var(--pink-text); }
  .poster-christmas .hero { top: 228px; left: 0; right: 0; height: 300px;
    background: linear-gradient(180deg, var(--mauve), #b97894 45%, #7a9a6a 78%, var(--green)); }
  .poster-christmas .photo { top: 229px; left: 96px; width: 205px; height: 120px;
    background: linear-gradient(135deg, #f0d9de, #c7394b 55%, #8d2a36); }
  .poster-christmas .offer-1 { top: 410px; font-size: 31px; }
  .poster-christmas .offer-2 { top: 445px; font-size: 31px; }
  .poster-christmas .footer { height: 60px; background: var(--pink); color: var(--white); }

  /* Pedicure */
  .poster-pedicure { left: 710px; top: 167px; width: 427px; height: 603px; }
  .poster-pedicure .brand { width: 280px; height: 147px; }
  .poster-pedicure .locator { width: 147px; height: 147px; }
  .poster-pedicure .body { top: 147px; left: 0; right: 0; height: 394px;
    background: linear-gradient(180deg, var(--pink) 0%, var(--pink) 48%, #f6c8df 72%, var(--white) 92%); }
  .poster-pedicure .title { top: 172px; left: 0; right: 0; text-align: center; font-size: 44px; color: var(--white); line-height: 1; }
  .poster-pedicure .title-2 { top: 217px; left: 0; right: 0; text-align: center; font-size: 32px; color: var(--white); }
  .poster-pedicure .lead { top: 264px; left: 0; right: 0; text-align: center;
    font-family: "Arimo", sans-serif; font-weight: 700; color: var(--white); font-size: 31px; }
  .poster-pedicure .lead-big { top: 304px; left: 0; right: 0; text-align: center;
    font-family: "Arimo", sans-serif; font-weight: 700; color: var(--white); font-size: 43px; }
  .poster-pedicure .connector { top: 362px; left: 0; right: 0; text-align: center;
    font-family: "Arimo", sans-serif; font-weight: 700; color: #333; font-size: 17px; }
  .poster-pedicure .free-1 { top: 386px; font-size: 37px; }
  .poster-pedicure .free-2 { top: 427px; font-size: 37px; }
  .poster-pedicure .free-3 { top: 468px; font-size: 37px; }
  .poster-pedicure .footer { height: 62px; background: var(--pink-soft); color: var(--ink); }

  /* Mothers Day */
  .poster-mothers { left: 318px; top: 261px; width: 381px; height: 550px; transform: rotate(2deg); z-index: 2; }
  .poster-mothers .brand { width: 245px; height: 120px; }
  .poster-mothers .brand-name { font-size: 40px; }
  .poster-mothers .locator { width: 136px; height: 120px; }
  .poster-mothers .locator-lead { font-size: 19px; }
  .poster-mothers .locator-store { font-size: 26px; }
  .poster-mothers .band { top: 120px; left: 0; right: 0; height: 110px;
    background: linear-gradient(180deg, var(--white), #fbe2ef); }
  .poster-mothers .title { top: 160px; left: 0; right: 0; text-align: center; font-size: 39px; color: var(--pink-text); }
  .poster-mothers .gift { top: 230px; left: 106px; width: 148px; height: 92px;
    background: linear-gradient(135deg, #f7cfe3, #d96aa6 60%, #c8323f); }
  .poster-mothers .voucher { top: 362px; font-size: 40px; }
  .poster-mothers .voucher-sub { top: 406px; font-size: 23px; }
  .poster-mothers .footer { height: 77px; background: var(--pink); color: var(--white); }
</style>
</head>
<body>
<main class="stage">

  <article class="poster poster-christmas">
    <div class="brand"><span class="brand-name">Lacquer</span><span class="brand-sub">Nail Salon</span></div>
    <div class="locator"><span class="locator-lead">FIND US<br>NEXT TO</span><span class="locator-store">TallMart</span></div>
    <h2 class="script title">Christmas in July!</h2>
    <div class="hero"></div>
    <div class="photo" role="img" aria-label="Photo of festive red and white manicured nails wrapped with a red gift bow"></div>
    <p class="punch offer-1">Purchase a set of nails</p>
    <p class="punch offer-2">and get a $10 gift voucher</p>
    <footer class="footer">www.lacquernailsalon.com.au</footer>
  </article>

  <article class="poster poster-pedicure">
    <div class="brand"><span class="brand-name">Lacquer</span><span class="brand-sub">Nail Salon</span></div>
    <div class="locator"><span class="locator-lead">FIND US<br>NEXT TO</span><span class="locator-store">TallMart</span></div>
    <div class="body"></div>
    <h2 class="script title">New Deluxe Pedicure</h2>
    <p class="script title-2">service</p>
    <p class="lead">Try our new Deluxe</p>
    <p class="lead-big">Spa Pedicure</p>
    <p class="connector">and get a</p>
    <p class="punch free-1">FREE nail buff,</p>
    <p class="punch free-2">shape and polish</p>
    <p class="punch free-3">for your fingernails</p>
    <footer class="footer">www.lacquernailsalon.com.au<span class="social-box"></span></footer>
  </article>

  <article class="poster poster-mothers">
    <div class="brand"><span class="brand-name">Lacquer</span><span class="brand-sub">Nail Salon</span></div>
    <div class="locator"><span class="locator-lead">FIND US<br>NEXT TO</span><span class="locator-store">TallMart</span></div>
    <div class="band"></div>
    <h2 class="script title">Mothers Day Special</h2>
    <div class="gift" role="img" aria-label="Illustration of a pink gift box tied with a red ribbon bow"></div>
    <p class="punch voucher">$10 gift voucher</p>
    <p class="punch voucher-sub">when you spend over $50</p>
    <footer class="footer">www.lacquernailsalon.com.au<span class="social-box"></span></footer>
  </article>

</main>
</body>
</html>
```